Tarvik Plans - Worpress Design

We are a consultancy to help builders to optimize their planning in order to save building costs. For that reason we need a website to offer our services, present our history, the mission and offer a plug-in for a first contact (including calendar), testimonials, a blog etc.
As an idea, I really like: https://www.fendrowadvisory.de/
Later on the website should be programmed in www.quelvo.de in our Wordpress area. The text, of course, will be done by myself. The colors should be suitable to our recently designed logo.

```html
<!DOCTYPE html>
<html lang="en">
<head>
<meta charset="utf-8">
<title>Tarvik Plans – Building Consultancy</title>
<link href="https://fonts.googleapis.com/css2?family=Poppins:wght@300;400;500;600;700;800&display=swap" rel="stylesheet">
<style>
:root{
  --gold:#c8913a;
  --gold-light:#f1d06b;
  --gold-dark:#b47a2a;
  --ink:#111111;
  --text:#444444;
  --muted:#777777;
  --line:#d8d8d8;
  --footer:#1d1d1d;
  --white:#ffffff;
  --photo-warm:#8a8073;
  --photo-cool:#5d6a70;
}
*{box-sizing:border-box;margin:0;padding:0}
html,body{width:1200px;height:4570px;overflow:hidden;background:var(--white)}
body{position:relative;font-family:'Poppins',sans-serif;color:var(--ink)}
.abs{position:absolute}
a{color:inherit;text-decoration:none}

/* header */
.brand{left:89px;top:24px;display:flex;align-items:center;gap:10px;font-weight:700;font-size:20px;color:var(--gold)}
.brand-mark{width:22px;height:22px;border:2px solid var(--gold)}
.nav{top:36px;right:88px;display:flex;gap:22px;font-size:12.5px;font-weight:600}
.nav a{position:relative}
.nav .active{color:var(--gold)}
.nav .active::before{content:"";position:absolute;left:0;right:0;top:-36px;height:4px;background:var(--gold)}

/* hero */
.hero-title{left:89px;top:148px;font-size:64px;line-height:68px;font-weight:800;letter-spacing:-.5px}
.hero-title .gold{color:var(--gold)}
.hero-lead{left:90px;top:290px;width:470px;font-size:14px;line-height:20px;color:var(--text)}
.btn-gold{left:90px;top:346px;width:137px;height:38px;background:linear-gradient(90deg,var(--gold-dark),var(--gold-light));color:var(--white);font-size:11px;font-weight:700;display:flex;align-items:center;justify-content:center}
.stat{top:196px}
.stat-num{font-size:34px;font-weight:400;line-height:44px}
.stat-num.gold{color:var(--gold)}
.stat-label{font-size:15px;line-height:23px;font-weight:500;margin-top:6px}
.stat-sep{top:200px;width:1px;height:90px;background:var(--line)}
.scroll-arrow{left:24px;top:488px}
.photo{background:linear-gradient(135deg,#b9b3aa,var(--photo-warm) 55%,#4b4f55)}
.hero-photo{left:89px;top:444px;width:1111px;height:582px}
.hero-photo-top{left:316px;top:328px;width:310px;height:120px}
.outline-word{font-weight:700;color:transparent;-webkit-text-stroke:4px var(--white);white-space:nowrap;overflow:hidden;line-height:1}
.hero-outline{left:89px;top:856px;width:621px;height:170px;font-size:200px}
.history-photo{left:710px;top:861px;width:490px;height:586px;background:linear-gradient(160deg,#9aa3a8,var(--photo-cool) 60%,#333)}

/* history */
.eyebrow{left:178px;top:1116px;display:flex;align-items:center;gap:12px;font-size:12px;font-weight:600}
.eyebrow::before{content:"";width:28px;height:2px;background:var(--ink)}
.history-title{left:178px;top:1142px;font-size:35px;line-height:46px;font-weight:800}
.history-text{left:178px;top:1242px;width:405px;font-size:14px;line-height:23px;color:var(--text)}
.read-more{left:180px;top:1408px;font-size:12px;font-weight:700;color:var(--gold);border-bottom:1px solid var(--gold)}

/* services */
.service{top:1543px;width:238px;height:277px;background:var(--white);box-shadow:0 18px 40px rgba(0,0,0,.09);padding:44px 44px 0}
.service.featured{background:linear-gradient(135deg,var(--gold-dark),var(--gold-light));color:var(--white)}
.service svg.icon{width:66px;height:66px}
.service h3{margin-top:36px;font-size:19px;line-height:25px;font-weight:700}
.service .go{margin-top:26px}
.view-all{left:0;width:1200px;top:1873px;text-align:center;font-size:12.5px;font-weight:700}
.view-all span{border-bottom:1.5px solid var(--ink)}

/* training band */
.training-photo{left:0;top:1970px;width:1200px;height:598px;background:linear-gradient(120deg,#6d7b82,#3e4a50 50%,#8c9296)}
.training-outline{left:-10px;top:2378px;width:1210px;height:190px;font-size:250px}

/* testimonials */
.quote-mark{left:39px;top:2690px}
.testi-title{left:119px;top:2744px;font-size:35px;line-height:40px;font-weight:800}
.arrow-btn{top:2840px;width:27px;height:27px;display:flex;align-items:center;justify-content:center}
.arrow-btn.prev{left:119px;background:var(--gold)}
.arrow-btn.next{left:151px;background:var(--ink)}
.testi-name{left:524px;font-size:22px;font-weight:600}
.testi-role{left:524px;font-size:15px;color:var(--text)}
.testi-text{left:733px;width:360px;font-size:14px;line-height:20px;color:var(--text)}
.testi-rule{left:515px;top:2812px;width:578px;height:2px;background:#bcbcbc}

/* articles */
.section-title{left:0;width:1200px;text-align:center;top:3032px;font-size:34px;font-weight:800}
.article{top:3103px;width:294px;height:367px;background:var(--white);box-shadow:0 14px 34px rgba(0,0,0,.08)}
.article .thumb{height:234px;background:linear-gradient(135deg,#d7d9db,#8a9299 60%,#4e555b)}
.article .body{padding:18px 30px 0}
.article .date{font-size:11px;color:var(--text)}
.article h4{margin-top:12px;font-size:14px;font-weight:700}
.article p{margin-top:10px;font-size:13px;line-height:18px;color:var(--text)}

/* contact */
.contact-title{left:135px;top:3642px;font-size:35px;font-weight:800}
.worker-photo{left:612px;top:3523px;width:524px;height:560px;background:linear-gradient(180deg,#f4efe4,#c9bda6 55%,#6c655a)}
.footer-bg{left:0;top:4083px;width:1200px;height:487px;background:var(--footer)}
.contact-form{left:119px;top:3703px;width:442px;height:424px;background:linear-gradient(120deg,var(--gold-dark),var(--gold-light));padding:0 25px}
.field-label{position:absolute;font-size:10px;font-weight:700;color:var(--white)}
.field{position:absolute;background:var(--white);font-size:11px;color:var(--muted);padding:0 16px;display:flex;align-items:center;justify-content:space-between}
.submit{position:absolute;left:25px;top:351px;width:392px;height:43px;background:var(--ink);color:var(--white);font-size:14px;font-weight:700;display:flex;align-items:center;justify-content:center}
.submit svg{position:absolute;right:18px}

/* footer */
.foot-head{top:4228px;font-size:18px;font-weight:700;color:var(--white)}
.foot-links{left:126px;top:4278px;list-style:none;font-size:12px;color:#cfcfcf;line-height:27px}
.info{left:335px;font-size:12px;line-height:17px;color:#cfcfcf;display:flex;gap:10px}
.news-text{left:600px;top:4300px;width:260px;font-size:12px;line-height:17px;color:#cfcfcf}
.news-input{left:602px;top:4333px;width:246px;height:46px;background:var(--white);font-size:12px;color:var(--muted);display:flex;align-items:center;padding:0 18px;gap:8px}
.social{top:4318px;width:40px;height:40px;border-radius:50%;background:#2e2e2e}
.foot-rule{left:89px;top:4517px;width:1022px;height:1px;background:#3a3a3a}
.copyright{left:0;width:1200px;top:4536px;text-align:center;font-size:12px;font-weight:500;color:var(--white)}
.to-top{left:1131px;top:4497px;width:46px;height:46px;border-radius:50%;background:linear-gradient(135deg,var(--gold-dark),var(--gold-light));display:flex;align-items:center;justify-content:center}
</style>
</head>
<body>

<!-- header -->
<div class="abs brand"><span class="brand-mark"></span>Tarvik Plans</div>
<nav class="abs nav">
  <a class="active">HOME</a><a>OUR HISTORY</a><a>SERVICES</a><a>MISSION</a><a>BLOG</a><a>CONTACT US</a>
</nav>

<!-- hero -->
<h1 class="abs hero-title">WELCOME TO<br><span class="gold">TARVIK</span> PLANS</h1>
<p class="abs hero-lead">We are a consultancy to help builders to optimize their planning in order to save building costs.</p>
<a class="abs btn-gold">GET A QUOTE</a>

<div class="abs stat" style="left:705px"><div class="stat-num gold">357+</div><div class="stat-label">People<br>Recruited</div></div>
<div class="abs stat-sep" style="left:836px"></div>
<div class="abs stat" style="left:875px"><div class="stat-num">100+</div><div class="stat-label">Happy<br>Clients</div></div>
<div class="abs stat-sep" style="left:990px"></div>
<div class="abs stat" style="left:1030px"><div class="stat-num">15+</div><div class="stat-label">Our<br>Countries</div></div>

<svg class="abs scroll-arrow" width="32" height="46" viewBox="0 0 32 46"><path d="M16 2v40M3 29l13 13 13-13" fill="none" stroke="#333" stroke-width="1.6"/></svg>

<div class="abs photo hero-photo-top" role="img" aria-label="Construction consultants in hard hats reviewing plans"></div>
<div class="abs photo hero-photo" role="img" aria-label="Two construction consultants in white hard hats reviewing a tablet in front of apartment buildings"></div>
<div class="abs outline-word hero-outline">TARVIK</div>
<div class="abs history-photo" role="img" aria-label="Site worker in yellow hard hat and safety vest with a consultant holding a tablet"></div>
<svg class="abs" style="left:930px;top:1112px" width="56" height="56" viewBox="0 0 56 56"><circle cx="28" cy="28" r="26" fill="none" stroke="#fff" stroke-width="2"/><path d="M23 19l13 9-13 9z" fill="#fff"/></svg>

<!-- history -->
<div class="abs eyebrow">OUR HISTORY</div>
<h2 class="abs history-title">WHAT THE BUSINESS<br>IS TARVIK PLANS</h2>
<p class="abs history-text">It is a long established fact that a reader will be distracted by the readable content of a page when looking at its layout. The point of using Lorem Ipsum is that it has a more-or-less normal distribution of letters, as opposed to using 'Content here, content here', making it look like readable English. Many desktop...</p>
<a class="abs read-more">READ MORE</a>

<!-- services -->
<div class="abs service" style="left:225px">
  <svg class="icon" viewBox="0 0 66 66" fill="none" stroke="#222" stroke-width="2"><rect x="8" y="20" width="38" height="26"/><path d="M20 56h14M27 46v10"/><circle cx="50" cy="16" r="7"/><circle cx="50" cy="16" r="2.5"/><path d="M14 28h18M14 34h24M14 40h12"/></svg>
  <h3>TRAINING &amp;<br>WORKSHOPS</h3>
  <svg class="go" width="22" height="16" viewBox="0 0 22 16"><path d="M1 8h19M13 1l7 7-7 7" fill="none" stroke="#333" stroke-width="1.5"/></svg>
</div>
<div class="abs service featured" style="left:481px">
  <svg class="icon" viewBox="0 0 66 66" fill="none" stroke="#fff" stroke-width="2"><rect x="14" y="6" width="40" height="52"/><path d="M22 16h24M22 24h24"/><path d="M34 30l10 4v8c0 6-5 10-10 12-5-2-10-6-10-12v-8z"/><path d="M29 42l4 4 7-8"/></svg>
  <h3>REGULATORY<br>COMPLIANCE</h3>
  <svg class="go" width="22" height="16" viewBox="0 0 22 16"><path d="M1 8h19M13 1l7 7-7 7" fill="none" stroke="#fff" stroke-width="1.5"/></svg>
</div>
<div class="abs service" style="left:738px">
  <svg class="icon" viewBox="0 0 66 66" fill="none" stroke="#222" stroke-width="2"><circle cx="16" cy="42" r="11"/><path d="M16 35v14M12 38h6M12 46h6"/><rect x="32" y="44" width="6" height="14"/><rect x="42" y="36" width="6" height="22"/><rect x="52" y="28" width="6" height="30"/><circle cx="46" cy="14" r="7"/><circle cx="46" cy="14" r="2.5"/></svg>
  <h3>COST<br>OPTIMIZATION</h3>
  <svg class="go" width="22" height="16" viewBox="0 0 22 16"><path d="M1 8h19M13 1l7 7-7 7" fill="none" stroke="#333" stroke-width="1.5"/></svg>
</div>
<div class="abs view-all"><span>VIEW ALL SERVICES</span></div>

<!-- training band -->
<div class="abs training-photo" role="img" aria-label="Consultants and engineers in hard hats shaking hands beside a modern glass building"></div>
<div class="abs outline-word training-outline">TRAINING</div>

<!-- testimonials -->
<svg class="abs quote-mark" width="112" height="90" viewBox="0 0 112 90"><path d="M4 90V52C4 24 18 8 46 4v16C32 24 26 34 26 48h22v42zM62 90V52C62 24 76 8 104 4v16C90 24 84 34 84 48h22v42z" fill="#ececec"/></svg>
<h2 class="abs testi-title">CLIENT'S<br>TESTIMONIALS</h2>
<div class="abs arrow-btn prev"><svg width="8" height="10" viewBox="0 0 8 10"><path d="M6 1L2 5l4 4" fill="none" stroke="#fff" stroke-width="1.5"/></svg></div>
<div class="abs arrow-btn next"><svg width="8" height="10" viewBox="0 0 8 10"><path d="M2 1l4 4-4 4" fill="none" stroke="#fff" stroke-width="1.5"/></svg></div>

<div class="abs testi-name" style="top:2704px">Jhon Smith</div>
<div class="abs testi-role" style="top:2733px">Owner</div>
<p class="abs testi-text" style="top:2678px">There are many variations of passages of Lorem Ipsum available, but the majority have suffered alteration in some form, by injected humour, or randomised words which don't look even slightly believable.</p>
<div class="abs testi-rule"></div>
<div class="abs testi-name" style="top:2874px">Jhon Smith</div>
<div class="abs testi-role" style="top:2903px">Owner</div>
<p class="abs testi-text" style="top:2848px">There are many variations of passages of Lorem Ipsum available, but the majority have suffered alteration in some form, by injected humour, or randomised words which don't look even slightly believable.</p>

<!-- articles -->
<h2 class="abs section-title">LATEST ARTICLES</h2>
<article class="abs article" style="left:146px">
  <div class="thumb" role="img" aria-label="Consultants in hard hats studying a large blueprint in an office"></div>
  <div class="body"><div class="date">25-05-2022</div><h4>SOME HEADING GOES HERE</h4><p>Aenean sollicitudin lorem quis nisi elit consequat ipsum nec...</p></div>
</article>
<article class="abs article" style="left:453px">
  <div class="thumb" role="img" aria-label="Team discussing a white architectural building model"></div>
  <div class="body"><div class="date">25-05-2022</div><h4>SOME HEADING GOES HERE</h4><p>Aenean sollicitudin lorem quis nisi elit consequat ipsum nec...</p></div>
</article>
<article class="abs article" style="left:760px">
  <div class="thumb" role="img" aria-label="Two site managers in hard hats pointing at a tower under construction"></div>
  <div class="body"><div class="date">25-05-2022</div><h4>SOME HEADING GOES HERE</h4><p>Aenean sollicitudin lorem quis nisi elit consequat ipsum nec...</p></div>
</article>

<!-- contact -->
<div class="abs footer-bg"></div>
<div class="abs worker-photo" role="img" aria-label="Builder in orange hard hat and overalls working on a laptop"></div>
<h2 class="abs contact-title">CONTACT US</h2>
<form class="abs contact-form">
  <span class="field-label" style="left:25px;top:32px">NAME*</span>
  <span class="field-label" style="left:225px;top:32px">EMAIL*</span>
  <div class="field" style="left:25px;top:51px;width:191px;height:30px">Enter your name</div>
  <div class="field" style="left:225px;top:51px;width:191px;height:30px">Enter your email
    <svg width="8" height="6" viewBox="0 0 8 6"><path d="M1 1l3 3 3-3" fill="none" stroke="#333" stroke-width="1.4"/></svg></div>
  <span class="field-label" style="left:25px;top:104px">PHONE*</span>
  <span class="field-label" style="left:225px;top:104px">DATE*</span>
  <div class="field" style="left:25px;top:122px;width:191px;height:32px">Enter phone number</div>
  <div class="field" style="left:225px;top:122px;width:191px;height:32px">Select date</div>
  <span class="field-label" style="left:25px;top:177px">MESSAGE*</span>
  <div class="field" style="left:25px;top:197px;width:392px;height:133px;align-items:flex-start;padding-top:12px">Type your text...</div>
  <div class="submit">SUBMIT NOW
    <svg width="18" height="16" viewBox="0 0 18 16"><path d="M1 7l16-6-5 14-3-6z" fill="#fff"/></svg></div>
</form>

<!-- footer -->
<div class="abs foot-head" style="left:126px">QUICK LINKS</div>
<ul class="abs foot-links"><li>HOME</li><li>OUR HISTORY</li><li>SERVICES</li><li>MISSION</li><li>BLOG</li><li>CONTACT US</li></ul>

<div class="abs foot-head" style="left:335px">CONTACT INFO</div>
<div class="abs info" style="top:4278px"><svg width="12" height="10" viewBox="0 0 12 10"><rect x=".5" y=".5" width="11" height="9" fill="var(--gold)"/><path d="M.5 .5l5.5 5 5.5-5" fill="none" stroke="#1d1d1d"/></svg><span>Email:<br>info@example.com</span></div>
<div class="abs info" style="top:4332px"><svg width="12" height="12" viewBox="0 0 12 12"><path d="M2 1l3 1 1 3-2 1c1 2 2 3 3 3l1-2 3 1 0 3c-6 0-9-4-9-10z" fill="var(--gold)"/></svg><span>Phone:<br>0123-456-789</span></div>
<div class="abs info" style="top:4386px"><svg width="12" height="14" viewBox="0 0 12 14"><path d="M6 13C2 8 1 6 1 5a5 5 0 0110 0c0 1-1 3-5 8z" fill="var(--gold)"/><circle cx="6" cy="5" r="2" fill="#1d1d1d"/></svg><span>Location:<br>Some gose address here</span></div>

<div class="abs foot-head" style="left:600px">NEWSLETTER</div>
<p class="abs news-text">Join our mailing list to learn about our latest projects and product offerings</p>
<div class="abs news-input">
  <svg width="12" height="9" viewBox="0 0 12 9"><rect x=".5" y=".5" width="11" height="8" fill="none" stroke="#999"/><path d="M.5 .5l5.5 4 5.5-4" fill="none" stroke="#999"/></svg>
  <span style="flex:1">Enter your email...</span>
  <svg width="16" height="14" viewBox="0 0 18 16"><path d="M1 7l16-6-5 14-3-6z" fill="var(--gold)"/></svg>
</div>
<div class="abs social" style="left:915px" aria-label="Social profile"></div>
<div class="abs social" style="left:969px" aria-label="Social profile"></div>
<div class="abs social" style="left:1020px" aria-label="Social profile"></div>
<div class="abs social" style="left:1070px" aria-label="Social profile"></div>

<div class="abs foot-rule"></div>
<div class="abs copyright">© 2023 All Rights Reserved | Tarvik Plans</div>
<div class="abs to-top"><svg width="12" height="14" viewBox="0 0 12 14"><path d="M6 13V2M1 6l5-5 5 5" fill="none" stroke="#fff" stroke-width="1.6"/></svg></div>

</body>
</html>
```